I am a company selling interior designing materials

HI, I am selling interior design materials and require a namecard which is more outstanding while following a certain details placement as attached.

My clients are mainly interior designers so it has to attract their attention rather than feeling that its "just another namecard". I am selling wallcoverings, fabrics, acoustics and carpets.

Target Market(s)

interior designers designing hotels, commerical offices.

Contact Information for Business Card

As per attached.
Please change address to 47 Jalan 16 Tampines #05-02 Velmora Building Singapore 527314

Font styles to use
Other font styles liked:
• calibri

Requirements
Must have
• (1) company logo on top in the middle. Placement of contac details to be the same
• (2) company color is blue/green cymk 75/8/42/0
• (3) "KTV" logo to be prominent
• (4) You may change the logo but there should be a "swirl" surrounding the word KTV like current logo. The swirl pattern does not need to follow current logo and you may propose.
Should not have
• (1) there should not be any designs above "KTV" logo
• (2) no sharp triangles or angles

```html
<!DOCTYPE html>
<html lang="en">
<head>
<meta charset="utf-8">
<title>KTV Business Card</title>
<link href="https://fonts.googleapis.com/css2?family=Open+Sans:wght@400;600;700&display=swap" rel="stylesheet">
<style>
  :root {
    --teal: #1fb0a4;
    --ink: #555555;
    --shade: #626262;
    --accent: #e8202a;
    --paper: #ffffff;
    --backdrop: #6b6b6b;
  }
  * { margin: 0; padding: 0; box-sizing: border-box; }
  html, body { width: 1200px; height: 802px; overflow: hidden; background: var(--backdrop); }
  .stage { position: relative; width: 1200px; height: 802px; }
  .card {
    position: absolute;
    top: 274px;
    width: 545px;
    height: 325px;
    background: var(--teal);
    overflow: hidden;
    transform: scale(0.8128);
    transform-origin: 0 0;
    box-shadow: 4px 5px 8px rgba(0,0,0,0.45);
    font-family: "Open Sans", sans-serif;
  }
  .card--front { left: 136px; }
  .card--back { left: 624px; }
  .card__shapes { position: absolute; inset: 0; }
  .card__text { position: absolute; left: 0; width: 100%; text-align: center; }
  .wordmark { font-weight: 700; color: var(--ink); letter-spacing: 1px; line-height: 1; }
  .card--front .wordmark { top: 58px; font-size: 38px; }
  .card--back .wordmark { top: 80px; font-size: 66px; }
  .company { top: 118px; font-size: 13px; font-weight: 700; color: var(--ink); }
  .person { top: 150px; font-size: 23px; font-weight: 400; color: var(--teal); }
  .address { top: 193px; font-size: 14px; line-height: 19px; color: var(--ink); }
  .contacts { top: 280px; font-size: 14px; color: var(--paper); }
  .contacts b { font-weight: 700; }
  .services { top: 279px; font-size: 16px; color: var(--paper); word-spacing: 1px; }
</style>
</head>
<body>
<div class="stage">

  <div class="card card--front">
    <svg class="card__shapes" viewBox="0 0 545 325" aria-hidden="true">
      <ellipse cx="292" cy="108" rx="300" ry="158" transform="rotate(-5 292 108)" fill="var(--shade)"/>
      <ellipse cx="286" cy="100" rx="298" ry="156" transform="rotate(-5 286 100)" fill="var(--paper)"/>
    </svg>
    <div class="card__text wordmark">KTV</div>
    <div class="card__text company">Kentavi Interior Furnishings Pte Ltd</div>
    <div class="card__text person">Lorna Chua</div>
    <div class="card__text address">47 Jalan 16 Tampines #05-02<br>Velmora Building Singapore 527314</div>
    <div class="card__text contacts"><b>P:</b> (65)9172 4406 &nbsp;| <b>M:</b> (65)6281 3057 &nbsp;| <b>E:</b> lorna@ktvfurnishings.com</div>
  </div>

  <div class="card card--back">
    <svg class="card__shapes" viewBox="0 0 545 325" aria-hidden="true">
      <ellipse cx="292" cy="110" rx="300" ry="158" transform="rotate(-5 292 110)" fill="var(--accent)"/>
      <ellipse cx="286" cy="100" rx="298" ry="156" transform="rotate(-5 286 100)" fill="var(--paper)"/>
    </svg>
    <div class="card__text wordmark">KTV</div>
    <div class="card__text services">Wallcoverings | Acoustic &nbsp;| Fabrics &nbsp;| Carpet</div>
  </div>

</div>
</body>
</html>
```